Motorcycle Shop Business Card

New business card for Motorcycle repair and customization shop.Business name: Steel Falcon Chris Morris443-865-5190, 2817 Harbor Lane Corvale, WN 21094. www.dana@steelfalconcycles.example. I uploaded some motorcycle images and logo and a couple of our calendar shoots. They do not have to be used on card just examples of some of our work and past graphic work.
We work on Kestrel Brandt and Custom Built Motorcycles.

Looking for front and back design

Motorcycle owners

```html
<!DOCTYPE html>
<html lang="en">
<head>
<meta charset="utf-8">
<title>Steel Falcon Customs – Business Card</title>
<link href="https://fonts.googleapis.com/css2?family=Roboto:wght@400;700&display=swap" rel="stylesheet">
<style>
  :root {
    --page-bg: #a9a9a9;
    --card-bg: #ffffff;
    --ink: #1a1a1a;
    --ink-soft: #6f6f6f;
    --rule: #9a9a9a;
    --band-dark: #111111;
    --band-grey: #b5b5b5;
    --photo-light: #f4f8f9;
    --photo-mid: #cfe6ea;
    --photo-chrome: #9ea4a8;
  }
  * { box-sizing: border-box; margin: 0; padding: 0; }
  html, body { width: 1200px; height: 885px; overflow: hidden; }
  body {
    background: var(--page-bg);
    font-family: "Roboto", Arial, sans-serif;
    color: var(--ink);
    position: relative;
  }
  .card {
    position: absolute;
    width: 560px;
    height: 320px;
    background: var(--card-bg);
    box-shadow: 0 10px 24px rgba(0,0,0,0.3);
    overflow: hidden;
  }
  .card--front { left: 50px; top: 90px; }
  .card--back { left: 590px; top: 475px; }

  .brand {
    position: absolute;
    display: flex;
    align-items: center;
    gap: 10px;
    font-weight: 700;
    color: var(--ink);
    line-height: 1.05;
  }
  .brand__mark {
    width: 14px; height: 14px;
    border-radius: 50%;
    background: var(--ink);
    flex: none;
  }
  .brand__name { font-size: 26px; }
  .card--front .brand { right: 50px; top: 28px; }
  .card--back .brand { right: 70px; top: 40px; }

  .bike-photo {
    position: absolute;
    left: 0; top: 100px;
    width: 470px; height: 220px;
    background:
      radial-gradient(ellipse at 75% 45%, var(--photo-chrome) 0%, transparent 35%),
      radial-gradient(ellipse at 30% 65%, var(--photo-chrome) 0%, transparent 40%),
      linear-gradient(160deg, var(--photo-light) 0%, var(--photo-mid) 55%, var(--photo-light) 100%);
  }

  .divider {
    position: absolute;
    left: 40px; right: 40px;
    height: 1px;
    background: var(--rule);
  }
  .divider--top { top: 128px; }
  .divider--name { top: 236px; left: 40px; right: 250px; }

  .address {
    position: absolute;
    right: 40px; top: 142px;
    text-align: right;
    font-size: 14px;
    line-height: 1.4;
    color: var(--ink-soft);
  }
  .holder-name {
    position: absolute;
    left: 40px; top: 204px;
    font-size: 22px;
    font-weight: 700;
    letter-spacing: 0.3px;
  }
  .contact {
    position: absolute;
    left: 40px; top: 245px;
    list-style: none;
    font-size: 14px;
    color: var(--ink-soft);
  }
  .contact li {
    display: flex;
    align-items: center;
    gap: 8px;
    height: 20px;
  }
  .contact svg { width: 12px; height: 12px; fill: var(--ink); }

  .footer-band {
    position: absolute;
    left: 0; bottom: 0;
    width: 100%; height: 16px;
  }
</style>
</head>
<body>

  <section class="card card--front" aria-label="Card front">
    <div class="brand">
      <span class="brand__mark"></span>
      <span class="brand__name">Steel Falcon<br>Customs</span>
    </div>
    <div class="bike-photo" role="img" aria-label="Photo of a white and pale blue custom chopper motorcycle with chrome engine and front wheel"></div>
  </section>

  <section class="card card--back" aria-label="Card back">
    <div class="brand">
      <span class="brand__mark"></span>
      <span class="brand__name">Steel Falcon<br>Customs</span>
    </div>
    <div class="divider divider--top"></div>
    <p class="address">2817 Harbor Lane<br>Corvale, WN 21094.</p>

    <h1 class="holder-name">DANA WHITLOCK</h1>
    <div class="divider divider--name"></div>
    <ul class="contact">
      <li>
        <svg viewBox="0 0 24 24" aria-hidden="true"><path d="M6.6 10.8a15.1 15.1 0 0 0 6.6 6.6l2.2-2.2a1 1 0 0 1 1-.25 11.4 11.4 0 0 0 3.6.57 1 1 0 0 1 1 1V20a1 1 0 0 1-1 1A17 17 0 0 1 3 4a1 1 0 0 1 1-1h3.5a1 1 0 0 1 1 1c0 1.25.2 2.45.57 3.6a1 1 0 0 1-.25 1z"/></svg>
        410-372-6814
      </li>
      <li>
        <svg viewBox="0 0 24 24" aria-hidden="true"><circle cx="12" cy="12" r="10"/></svg>
        www.dana@steelfalconcycles.example
      </li>
    </ul>

    <svg class="footer-band" viewBox="0 0 560 16" preserveAspectRatio="none" aria-hidden="true">
      <rect x="330" y="0" width="230" height="16" fill="var(--band-grey)"/>
      <polygon points="0,0 350,0 335,16 0,16" fill="var(--band-dark)"/>
    </svg>
  </section>

</body>
</html>
```